100% Organic Beard Care Product labels

We need labels for our organic beard care products, this includes 30ml matt black bottles, 50ml matt black jars and 100ml matt black boston bottles.
We have six beard oil products, three beard balm products, and one beard shampoo.
Would like white on black, or white on transparent print and logo.
Logo is attached along with an idea of label for our unscented product.

Target Market(s)

Mens beard care

Font styles to use
Other font styles liked:
• Verdana

```html
<!DOCTYPE html>
<html lang="en">
<head>
<meta charset="utf-8">
<title>Crownfield Grooming – Beard Oil Label</title>
<link href="https://fonts.googleapis.com/css2?family=Arimo:wght@400;700&family=Open+Sans:wght@400;700&display=swap" rel="stylesheet">
<style>
  :root {
    --ink: #0c0c0c;
    --paper: #ffffff;
    --rule: #8a8a8a;
    --ghost: #1a1a1a;
    --ghost-text: #232323;
    --stage: #ffffff;
  }
  html, body { margin: 0; padding: 0; }
  body {
    width: 1200px; height: 1200px; overflow: hidden;
    background: var(--stage);
    position: relative;
    font-family: "Arimo", Arial, sans-serif;
  }
  .label {
    position: absolute; left: 30px; top: 350px;
    width: 1140px; height: 499px;
    background: var(--ink); color: var(--paper);
    overflow: hidden;
  }
  .rule { position: absolute; height: 2px; background: var(--rule); }
  .rule--top-left { left: 0; top: 15px; width: 420px; }
  .rule--top-right { left: 596px; top: 15px; width: 544px; }
  .rule--bottom { left: 0; top: 480px; width: 1140px; }

  .usage { position: absolute; left: 33px; top: 43px; width: 225px; }
  .usage__title { font-weight: 700; font-size: 14px; letter-spacing: .3px; margin: 0 0 2px; }
  .usage__text { font-size: 13px; line-height: 17px; margin: 0; text-align: justify; }

  .warning { position: absolute; left: 32px; top: 143px; width: 220px; height: 40px; }
  .warning svg { position: absolute; left: 0; top: 0; }
  .warning__text {
    position: absolute; right: 0; top: 2px;
    font-weight: 700; font-size: 13px; line-height: 17px; text-align: right;
  }

  .marks { position: absolute; left: 33px; top: 303px; height: 50px; width: 200px; }
  .marks__brand {
    position: absolute; left: 0; top: 8px; width: 66px;
    display: flex; flex-direction: column; align-items: center; gap: 3px;
    font-family: "Open Sans", sans-serif; font-weight: 700; font-size: 8px;
    line-height: 9px; text-align: center;
  }
  .marks__dot { width: 14px; height: 14px; border-radius: 50%; background: var(--paper); }
  .marks__pao { position: absolute; left: 134px; top: 0; }

  .contact { position: absolute; left: 33px; top: 387px; font-weight: 700; font-size: 18px; line-height: 24px; }
  .contact p { margin: 0; }

  .banner { position: absolute; left: 446px; top: 0; }
  .banner__brand {
    position: absolute; left: 446px; top: 120px; width: 234px;
    display: flex; flex-direction: column; align-items: center; gap: 10px;
    color: var(--ink); font-family: "Open Sans", sans-serif; font-weight: 700;
    font-size: 22px; line-height: 24px; text-align: center;
  }
  .banner__dot { width: 26px; height: 26px; border-radius: 50%; background: var(--ink); }
  .banner__product {
    position: absolute; left: 446px; top: 261px; width: 234px; text-align: center;
    color: var(--ink); font-family: "Open Sans", sans-serif;
  }
  .banner__name {
    display: inline-block; font-weight: 700; font-size: 25px; line-height: 30px;
    letter-spacing: .5px; border-bottom: 2px solid var(--ink); padding: 0 2px 1px;
  }
  .banner__claim { font-size: 17px; line-height: 22px; }

  .variant {
    position: absolute; left: 446px; top: 402px; width: 234px; text-align: center;
    font-family: "Open Sans", sans-serif;
  }
  .variant__scent { font-size: 27px; line-height: 32px; }
  .variant__size { font-size: 14px; line-height: 18px; }

  .ghost-mark { position: absolute; left: 841px; top: 92px; width: 304px; height: 304px; border-radius: 50%; background: var(--ghost); }
  .ghost-name {
    position: absolute; left: 880px; top: 210px; width: 230px;
    font-family: "Open Sans", sans-serif; font-weight: 700; font-size: 34px; line-height: 40px;
    color: var(--ghost-text); transform: rotate(40deg); text-align: center;
  }

  .ingredients {
    position: absolute; left: 1040px; top: 465px; width: 423px;
    transform: rotate(-90deg); transform-origin: top left;
    font-family: "Open Sans", sans-serif; font-size: 13px; line-height: 17px;
    text-align: justify;
  }
  .ingredients strong { font-weight: 700; }
</style>
</head>
<body>
  <section class="label" aria-label="Crownfield Grooming beard oil label">
    <div class="rule rule--top-left"></div>
    <div class="rule rule--top-right"></div>
    <div class="rule rule--bottom"></div>

    <div class="usage">
      <h2 class="usage__title">HOW TO USE</h2>
      <p class="usage__text">Drop a small amount of oil onto the palm of your hand. rub your hands together then work the oil into the facial hair.</p>
    </div>

    <div class="warning">
      <svg width="38" height="36" viewBox="0 0 38 36" aria-hidden="true">
        <path d="M19 2 L36 34 H2 Z" fill="none" stroke="#fff" stroke-width="2.4" stroke-linejoin="round"/>
        <rect x="17.6" y="12" width="2.8" height="12" fill="#fff"/>
        <rect x="17.6" y="27" width="2.8" height="2.8" fill="#fff"/>
      </svg>
      <p class="warning__text" style="margin:0">Discontinue use if skin<br>irritation occurs</p>
    </div>

    <div class="marks">
      <div class="marks__brand"><span class="marks__dot"></span><span>CROWNFIELD GROOMING</span></div>
      <svg class="marks__pao" width="56" height="66" viewBox="0 0 56 66" aria-label="12 months after opening">
        <path d="M6 24 L48 6" stroke="#fff" stroke-width="5" stroke-linecap="round"/>
        <path d="M4 34 H52 V58 Q52 62 48 62 H8 Q4 62 4 58 Z" fill="#fff"/>
        <text x="28" y="55" text-anchor="middle" font-family="Arimo, sans-serif" font-weight="700" font-size="15" fill="#0c0c0c">12M</text>
      </svg>
    </div>

    <div class="contact">
      <p>crownfieldgrooming.co.uk</p>
      <p>Crownfield Grooming</p>
      <p>LN2 4QX</p>
    </div>

    <svg class="banner" width="234" height="400" viewBox="0 0 234 400" aria-hidden="true">
      <path d="M0 0 H234 V337 L117 392 L0 337 Z" fill="#fff"/>
      <path d="M12 0 V330 L117 380 L222 330 V0" fill="none" stroke="#0c0c0c" stroke-width="3"/>
    </svg>
    <div class="banner__brand"><span class="banner__dot"></span><span>CROWNFIELD<br>GROOMING</span></div>
    <div class="banner__product">
      <div class="banner__name">BEARD OIL</div>
      <div class="banner__claim">100% Organic</div>
    </div>

    <div class="variant">
      <div class="variant__scent">Unscented</div>
      <div class="variant__size">30ml</div>
    </div>

    <div class="ghost-mark"></div>
    <div class="ghost-name">CROWNFIELD GROOMING</div>

    <p class="ingredients"><strong>INGREDIENTS:</strong> Organic Grapeseed Oil (Vitis Vinifera), Organic Sweet Almond Oil (Peunus Dulcis), Organic Jojoba (Simondsia Chinesis), Organic Castrol Oil (Ricinus Communis Seed oil), Organic Argan Oil (Argania Spinosa).</p>
  </section>
</body>
</html>
```